Meridale Legal Letterhead for Law firm must be modern and use the logo I uploaded.

Hello I want a clean modern professional letterhead for my law firm Meridale Legal. A logo has already been created and all files have been uploaded. The information for the firm can be given through message. Please use the logo that has already been created. Please also use the color scheme of that logo. (blue and white).

Target Market(s)

General Public

Industry/Entity Type

Law Firm

Colors

Designer to choose colors to be used in the design.

Requirements
Must have
• This must be a modern professional letterhead
Nice to have
• My logo that is included in file form
Should not have
• Should not have logo that is not the one I uploaded.

```html
<!DOCTYPE html>
<html lang="en">
<head>
<meta charset="utf-8">
<title>Meridale Legal Letterhead</title>
<link rel="stylesheet" href="https://fonts.googleapis.com/css2?family=Roboto:wght@500&family=Source+Sans+3:wght@400&display=swap">
<style>
  :root {
    --navy-deep: #141a31;
    --navy: #252b62;
    --paper: #ffffff;
    --ink: #7a7b7f;
    --on-navy: #ffffff;
  }
  * { box-sizing: border-box; margin: 0; padding: 0; }
  html, body { width: 960px; height: 1200px; overflow: hidden; background: var(--paper); }
  .letterhead {
    position: relative;
    width: 960px;
    height: 1200px;
    background: var(--paper);
    font-family: "Source Sans 3", sans-serif;
    color: var(--ink);
  }
  .masthead {
    height: 228px;
    background: linear-gradient(100deg, var(--navy-deep) 0%, #1c2147 50%, var(--navy) 100%);
    position: relative;
    color: var(--on-navy);
  }
  .brand {
    position: absolute;
    left: 72px;
    top: 150px;
    display: flex;
    align-items: center;
    gap: 14px;
    font-family: "Roboto", sans-serif;
    font-weight: 500;
    font-size: 23px;
    letter-spacing: 6px;
    text-transform: uppercase;
  }
  .brand-mark { width: 12px; height: 12px; background: var(--on-navy); }
  .contact {
    position: absolute;
    left: 702px;
    top: 74px;
    list-style: none;
    font-size: 15px;
    line-height: 19px;
  }
  .contact li { display: flex; align-items: flex-start; gap: 12px; }
  .contact li.address { margin-bottom: 16px; }
  .contact svg { width: 14px; height: 14px; flex: none; margin-top: 2px; fill: none; stroke: var(--on-navy); stroke-width: 1.6; }
  .contact svg .solid { fill: var(--on-navy); stroke: none; }
  .letter-body {
    position: absolute;
    left: 61px;
    right: 61px;
    top: 335px;
    font-size: 17px;
    line-height: 22px;
  }
  .salutation { margin-left: 21px; margin-bottom: 54px; }
  .letter-body p.para { text-align: justify; margin-bottom: 22px; }
  .letter-body p.para.first { text-indent: 56px; }
</style>
</head>
<body>
<div class="letterhead">
  <header class="masthead">
    <div class="brand"><span class="brand-mark"></span>Meridale Legal</div>
    <ul class="contact">
      <li class="address">
        <svg viewBox="0 0 14 14"><path class="solid" d="M7 0a5 5 0 0 0-5 5c0 3.6 5 9 5 9s5-5.4 5-9a5 5 0 0 0-5-5zm0 7a2 2 0 1 1 0-4 2 2 0 0 1 0 4z"/></svg>
        <span>suit # 00, Lorem ipsum<br>Lorem Lorem ipsum</span>
      </li>
      <li>
        <svg viewBox="0 0 14 14"><path d="M3 1.5l2 2.5-1.2 1.5a8 8 0 0 0 4.7 4.7L10 9l2.5 2-1.3 2A11 11 0 0 1 1 2.8z"/></svg>
        <span>000-000-0000</span>
      </li>
      <li>
        <svg viewBox="0 0 14 14"><rect x="1" y="3" width="12" height="9"/><path d="M1 3l6 5 6-5"/></svg>
        <span>info@meridalelegal.com</span>
      </li>
      <li>
        <svg viewBox="0 0 14 14"><circle cx="7" cy="7" r="6"/><ellipse cx="7" cy="7" rx="2.6" ry="6"/><path d="M1 7h12"/></svg>
        <span>www.meridalelegal.com</span>
      </li>
    </ul>
  </header>

  <main class="letter-body">
    <p class="salutation">Dear Sir</p>
    <p class="para first">Lorem ipsum dolor sit amet, consectetur adipiscing elit. Integer eu odio mattis, pulvinar turpis quis, faucibus nisl. Proin feugiat, erat vitae cursus pharetra, enim est semper ligula, in malesuada orci nisl et diam. Etiam elementum metus ac fringilla vulputate. Etiam mattis ligula sed ante mollis bibendum. Orci varius natoque penatibus et magnis dis parturient montes, nascetur ridiculus mus.</p>
    <p class="para">Ut nibh augue, blandit ac orci ac, rutrum congue enim. Suspendisse gravida vulputate felis, quis interdum orci tincidunt quis. Praesent imperdiet maximus neque. Mauris ut dui enim. Nullam at efficitur elit. Donec ante ipsum, fermentum at lectus vel, blandit vulputate ante. Proin luctus suscipit diam id vestibulum. Morbi malesuada id mauris eget ullamcorper.</p>
    <p class="para">Donec varius orci purus, vitae aliquam libero volutpat id. Integer sed imperdiet libero. Aliquam accumsan, risus sit amet ornare consectetur, turpis felis dictum justo, non rhoncus mauris dui sed velit. Pellentesque habitant morbi tristique senectus et netus et malesuada fames ac turpis egestas. Pellentesque tincidunt vitae ligula nec imperdiet. Donec sed congue enim. Nullam elementum faucibus nulla nec vestibulum. Sed at tempor ligula. In quis vulputate nunc. Integer at gravida lacus, ac tristique risus. Sed at vulputate nulla.</p>
    <p class="para">Praesent blandit nunc eu efficitur commodo. In tempor nisi ex, vel venenatis ante vestibulum a. Duis vestibulum nibh a erat sagittis, nec euismod lorem varius. Nam ultricies turpis sed justo sollicitudin volutpat. Morbi sed mollis eros. Sed quis tortor id enim vehicula porttitor. Curabitur non aliquam ex. Phasellus dignissim fermentum elit, at finibus ligula mattis eget.</p>
  </main>
</div>
</body>
</html>
```